Web Application UI Design

Looking for a light weight UI re-design with complete html files and images for an existing project. As you can see from the uploaded files, the current design is clunky. We are looking to redesign the web application with state of the art light weight UI (Must include bootstrap and should be able to support angular)

Requirements
Must have
• Must have lightweight design preferably with material and bootstrap design
Nice to have
• The screen shots I uploaded show that the design is clunky. I am looking for some new designs

```html
<!DOCTYPE html>
<html lang="en">
<head>
<meta charset="UTF-8">
<title>NovaDesk — Login</title>
<link href="https://fonts.googleapis.com/css2?family=Source+Sans+3:wght@400;600;700&display=swap" rel="stylesheet">
<style>
  :root {
    --page-bg: #f9f9f9;
    --card-bg: #ffffff;
    --field-bg: #f5f5f5;
    --brand-blue: #1d2ee6;
    --button-blue: #2c3cf4;
    --text-dark: #2b2b2b;
    --placeholder: #6d6d6d;
    --white: #ffffff;
  }
  * { box-sizing: border-box; margin: 0; padding: 0; }
  html, body {
    width: 1200px;
    height: 675px;
    overflow: hidden;
  }
  body {
    background: var(--page-bg);
    font-family: "Source Sans 3", "Source Sans Pro", Arial, sans-serif;
    position: relative;
  }
  .login-title {
    position: absolute;
    top: 176px;
    left: 0;
    width: 1200px;
    text-align: center;
    font-size: 23px;
    font-weight: 700;
    color: var(--brand-blue);
    letter-spacing: 0.2px;
  }
  .login-subtitle {
    position: absolute;
    top: 221px;
    left: 0;
    width: 1200px;
    text-align: center;
    font-size: 13.5px;
    font-weight: 400;
    color: var(--text-dark);
  }
  .login-card {
    position: absolute;
    left: 432px;
    top: 268px;
    width: 334px;
    height: 228px;
    background: var(--card-bg);
    border-radius: 5px;
    box-shadow: 0 2px 10px rgba(0, 0, 0, 0.06);
  }
  .login-field {
    position: absolute;
    left: 13px;
    width: 309px;
    height: 33px;
    border: none;
    border-radius: 3px;
    background: var(--field-bg);
    padding: 0 10px;
    font-family: inherit;
    font-size: 12px;
    color: var(--text-dark);
    outline: none;
  }
  .login-field::placeholder { color: var(--placeholder); }
  .login-field--username { top: 25px; }
  .login-field--password { top: 75px; }
  .forgot-link {
    position: absolute;
    right: 12px;
    top: 128px;
    font-size: 12px;
    font-weight: 700;
    color: var(--brand-blue);
    text-decoration: none;
  }
  .login-button {
    position: absolute;
    left: 116px;
    top: 171px;
    width: 102px;
    height: 29px;
    border: none;
    border-radius: 4px;
    background: var(--button-blue);
    color: var(--white);
    font-family: inherit;
    font-size: 12px;
    font-weight: 700;
    box-shadow: 0 2px 4px rgba(44, 60, 244, 0.25);
    cursor: pointer;
  }
</style>
</head>
<body>
  <h1 class="login-title">Welcome to NovaDesk</h1>
  <p class="login-subtitle">Please Login to continue!</p>
  <form class="login-card">
    <input class="login-field login-field--username" type="text" placeholder="Username">
    <input class="login-field login-field--password" type="password" placeholder="Password">
    <a class="forgot-link" href="#">Forgot Password?</a>
    <button class="login-button" type="button">Login</button>
  </form>
</body>
</html>
```